Commercial Construction Interior Fitout company needs Logo and Business Cards

We need a logo and business card design. We specialise in Commercial Ceilings, Partitions, Plastering and Carpentry.

Company name: 7QX Commercial Interiors. Would like a professional looking card more than a fancy look. Gloss front preferably black pattern with Fluro Green and white text.

Will need:

Name
Position
Phone
Fax
Email
Postal Address
Web address
Updates

Thank you so much everyone for your efforts and fantastic designs..   If I didn't respond to everyone personally,  my apologises. 

Again, thanks all

R.M                               

Target Market(s)

Existing & New clients in the Construction Industry

Industry/Entity Type

Business

Requirements
Nice to have
• 7QX to be overlapped or made into some sort of Logo

```html
<!DOCTYPE html>
<html lang="en">
<head>
<meta charset="utf-8">
<title>7QX Commercial Interiors – Business Card</title>
<link rel="stylesheet" href="https://fonts.googleapis.com/css2?family=Arimo:wght@400;700&display=swap">
<style>
  :root {
    --backdrop: #e4e2df;
    --card-white: #ffffff;
    --card-black: #050505;
    --strip-black: #111111;
    --brand-red: #e3262d;
    --accent-fluro: #39ff14;
    --accent-fluro-dark: #2fb81a;
    --name-olive: #8c7a2c;
    --ink-teal: #1f3d45;
    --ink-grey: #4a5a60;
    --rule-red: #e07a7a;
    --band-cyan: #5fd0e0;
    --band-red: #ee3a2a;
    --band-green: #7cc242;
    --band-yellow: #f2c21a;
    --band-grey: #a9b0b4;
    --band-orange: #f5a623;
  }
  * { margin: 0; padding: 0; box-sizing: border-box; }
  html, body { width: 900px; height: 1200px; overflow: hidden; }
  body {
    background: var(--backdrop);
    font-family: "Arimo", Arial, sans-serif;
    position: relative;
  }
  .card {
    position: absolute;
    left: 120px;
    width: 660px;
    height: 377px;
    overflow: hidden;
    box-shadow: 0 10px 28px rgba(0,0,0,0.25);
  }
  /* Front side */
  .card-front { top: 130px; background: var(--card-white); }
  .front-strip {
    position: absolute; left: 0; top: 0; bottom: 0; width: 132px;
    background: linear-gradient(160deg, #1c1c1c, var(--strip-black) 55%, #000);
    display: flex; align-items: center; justify-content: center;
  }
  .strip-brand {
    writing-mode: vertical-rl;
    transform: rotate(180deg);
    color: var(--brand-red);
    font-weight: 700;
    font-size: 28px;
    line-height: 1.1;
    text-transform: uppercase;
    letter-spacing: 1px;
    text-align: center;
  }
  .accent-field {
    position: absolute; left: 380px; top: 100px; width: 280px; height: 277px;
    background: radial-gradient(ellipse at 100% 30%, rgba(227,38,45,0.22), rgba(227,38,45,0) 70%);
  }
  .holder {
    position: absolute; right: 36px; top: 30px; text-align: right;
  }
  .holder-name {
    color: var(--name-olive); font-weight: 700; font-size: 22px; letter-spacing: 1px;
  }
  .holder-position {
    margin-top: 6px;
    color: var(--accent-fluro-dark); font-weight: 700; font-size: 13px; letter-spacing: 2px;
    text-transform: uppercase;
  }
  .contact {
    position: absolute; left: 170px; top: 180px; width: 300px;
    color: var(--ink-teal);
  }
  .contact-address { font-weight: 700; font-size: 15px; line-height: 1.35; }
  .contact-rule { height: 1px; background: var(--rule-red); margin: 10px 0; width: 280px; }
  .contact-line { font-weight: 700; font-size: 13px; line-height: 1.7; color: var(--ink-grey); }
  /* Back side */
  .card-back { top: 690px; background: var(--card-black); }
  .band {
    position: absolute; left: 0; right: 0; height: 62px;
    background: linear-gradient(90deg, var(--band-cyan), var(--band-red) 22%, var(--band-green) 45%, var(--band-yellow) 62%, var(--band-grey) 82%, var(--band-orange));
    opacity: 0.9;
  }
  .band-top { top: 0; }
  .band-bottom { bottom: 0; }
  .back-brand {
    position: absolute; left: 0; right: 0; top: 150px;
    text-align: center; color: var(--brand-red);
    font-weight: 700; font-size: 34px; text-transform: uppercase; letter-spacing: 1px; line-height: 1.2;
  }
  .back-rule {
    position: absolute; left: 270px; right: 270px; top: 248px; height: 3px;
    background: var(--accent-fluro);
  }
</style>
</head>
<body>
  <section class="card card-front">
    <div class="front-strip">
      <div class="strip-brand">7QX Commercial<br>Interiors</div>
    </div>
    <div class="accent-field" role="img" aria-label="Decorative red sweep across the card face"></div>
    <div class="holder">
      <p class="holder-name">YOUR NAME HERE</p>
      <p class="holder-position">Position Title</p>
    </div>
    <div class="contact">
      <p class="contact-address">Address Line 1, Address Line 2<br>Address Line 3 City, State 555</p>
      <div class="contact-rule"></div>
      <p class="contact-line">Phone : 011134455</p>
      <p class="contact-line">Fax : 011324455</p>
      <div class="contact-rule"></div>
      <p class="contact-line">info@company.com</p>
      <p class="contact-line">www.Companyname.com</p>
    </div>
  </section>

  <section class="card card-back">
    <div class="band band-top" role="img" aria-label="Multicoloured faceted pattern band"></div>
    <div class="back-brand">7QX Commercial<br>Interiors</div>
    <div class="back-rule"></div>
    <div class="band band-bottom" role="img" aria-label="Multicoloured faceted pattern band"></div>
  </section>
</body>
</html>
```